Simple elegant business card

General card for a fin and television director.
Just want name, email, phone and address.

Target Market(s)

Prospective employers

Industry/Entity Type

Business

Requirements
Must have
• As above
Nice to have
• Logo but not necessary.
Should not have
• Not too colourful or funky.
• Simplicity and elegance the way to go.

```html
<!DOCTYPE html>
<html lang="en">
<head>
<meta charset="utf-8">
<title>Nora Hale – Business Card</title>
<link rel="stylesheet" href="https://fonts.googleapis.com/css2?family=Mulish:wght@400;700&display=swap">
<style>
  :root {
    --backdrop: #2a2a2a;
    --paper: #f1f1f1;
    --ink: #333333;
    --ink-soft: #444444;
    --accent: #2489cb;
    --accent-deep: #1a7fbd;
    --rule-light: #e6eef4;
    --name-light: #e9f1f7;
  }
  * { margin: 0; padding: 0; box-sizing: border-box; }
  html, body {
    width: 1200px;
    height: 900px;
    overflow: hidden;
  }
  body {
    position: relative;
    background: var(--backdrop);
    font-family: "Mulish", "Century Gothic", sans-serif;
  }
  .card {
    position: absolute;
    left: 360px;
    width: 478px;
    height: 268px;
  }
  .card-front {
    top: 166px;
    background: var(--paper);
    border-radius: 0 30px 0 30px;
  }
  .card-back {
    top: 476px;
    background: var(--accent-deep);
    border-radius: 30px 0 30px 0;
  }
  .card-name {
    position: absolute;
    right: 28px;
    font-weight: 700;
    font-size: 21px;
    letter-spacing: 0.2px;
  }
  .card-front .card-name { top: 170px; color: var(--ink); }
  .card-back .card-name { top: 170px; color: var(--name-light); }
  .card-rule {
    position: absolute;
    left: 0;
    top: 201px;
    width: 450px;
    height: 4px;
  }
  .card-front .card-rule { background: var(--accent); }
  .card-back .card-rule { background: var(--rule-light); }
  .contact-line {
    position: absolute;
    right: 28px;
    top: 213px;
    font-size: 15px;
    color: var(--ink);
    white-space: nowrap;
  }
  .contact-line .divider {
    color: var(--accent);
    margin: 0 6px;
  }
  .contact-line .phone { font-size: 13px; }
  .address {
    position: absolute;
    right: 28px;
    top: 243px;
    font-size: 13px;
    color: var(--ink-soft);
    white-space: nowrap;
  }
</style>
</head>
<body>
  <section class="card card-front">
    <h1 class="card-name">Nora Hale</h1>
    <div class="card-rule"></div>
    <p class="contact-line">
      <span class="email">norahale@mail.com</span><span class="divider">|</span><span class="phone">+1 310 555 0142</span>
    </p>
    <p class="address">42 Harbor Lane, Bayview, CA 94000</p>
  </section>

  <section class="card card-back">
    <p class="card-name">Nora Hale</p>
    <div class="card-rule"></div>
  </section>
</body>
</html>
```